CFO services graphic design

I own a business consulting firm called Marlowe Consulting and we need a graphic for CFO services in our colours and branding. The attached file "CFO services to be put into Marlowe consulting theme", shows the content for the design. The two other files show the theme and colours for the new design.

```html
<!DOCTYPE html>
<html lang="en">
<head>
<meta charset="utf-8">
<title>CFO Services</title>
<link href="https://fonts.googleapis.com/css2?family=Manrope:wght@500;800&family=Barlow:wght@700&display=swap" rel="stylesheet">
<style>
  :root {
    --orange: #f39531;
    --blue: #1babe3;
    --navy: #1c2a48;
    --arrow-grey: #d9d9d9;
    --seg-1: #1e2b4a;
    --seg-2: #143f80;
    --seg-3: #143f80;
    --seg-4: #1aabe2;
    --seg-5: #325476;
    --seg-6: #3563a3;
    --seg-7: #4070b5;
    --seg-8: #3bb9ea;
    --bg: #ffffff;
  }
  html, body { margin: 0; padding: 0; overflow: hidden; background: var(--bg); }
  .canvas { width: 1200px; height: 1200px; display: block; }
  .orbit { fill: none; stroke: var(--orange); stroke-width: 30; }
  .node-gap { fill: var(--bg); }
  .ring-left { fill: none; stroke: var(--orange); stroke-width: 38; }
  .ring-right { fill: none; stroke: var(--blue); stroke-width: 38; }
  .hub-segment { fill: none; stroke-width: 62; }
  .hub-divider { stroke: var(--bg); stroke-width: 7; }
  .spoke { stroke: var(--arrow-grey); stroke-width: 4; }
  .spoke-head { fill: var(--arrow-grey); }
  .hub-title { font-family: "Barlow", sans-serif; font-weight: 700; font-size: 60px; fill: var(--orange); text-anchor: middle; }
  .node-label { font-family: "Manrope", sans-serif; font-weight: 800; font-size: 36px; fill: var(--navy); text-anchor: middle; }
  .node-label .regular { font-weight: 500; }
</style>
</head>
<body>
<svg class="canvas" viewBox="0 0 1920 1920" xmlns="http://www.w3.org/2000/svg" role="img" aria-label="Chief Financial Officer responsibilities diagram">
  <defs>
    <marker id="spoke-arrow" viewBox="0 0 10 10" refX="2" refY="5" markerWidth="6" markerHeight="6" orient="auto">
      <path class="spoke-head" d="M0 0 L10 5 L0 10 Z"/>
    </marker>
    <g id="node-ring">
      <circle class="node-gap" r="224"/>
      <path class="ring-left" d="M0 -197 A197 197 0 0 0 0 197"/>
      <path class="ring-right" d="M0 -197 A197 197 0 0 1 0 197"/>
    </g>
  </defs>

  <circle class="orbit" cx="966" cy="966" r="626"/>

  <g class="nodes">
    <use href="#node-ring" x="966" y="340"/>
    <use href="#node-ring" x="1409" y="523"/>
    <use href="#node-ring" x="1592" y="966"/>
    <use href="#node-ring" x="1409" y="1409"/>
    <use href="#node-ring" x="966" y="1592"/>
    <use href="#node-ring" x="523" y="1409"/>
    <use href="#node-ring" x="340" y="966"/>
    <use href="#node-ring" x="523" y="523"/>
  </g>

  <g class="spokes">
    <line class="spoke" x1="966" y1="640" x2="966" y2="596" marker-end="url(#spoke-arrow)"/>
    <line class="spoke" x1="1196" y1="736" x2="1224" y2="708" marker-end="url(#spoke-arrow)"/>
    <line class="spoke" x1="1292" y1="966" x2="1336" y2="966" marker-end="url(#spoke-arrow)"/>
    <line class="spoke" x1="1196" y1="1196" x2="1224" y2="1224" marker-end="url(#spoke-arrow)"/>
    <line class="spoke" x1="966" y1="1292" x2="966" y2="1336" marker-end="url(#spoke-arrow)"/>
    <line class="spoke" x1="736" y1="1196" x2="708" y2="1224" marker-end="url(#spoke-arrow)"/>
    <line class="spoke" x1="640" y1="966" x2="596" y2="966" marker-end="url(#spoke-arrow)"/>
    <line class="spoke" x1="736" y1="736" x2="708" y2="708" marker-end="url(#spoke-arrow)"/>
  </g>

  <g class="hub" transform="translate(966 966)">
    <path class="hub-segment" style="stroke:var(--seg-1)" d="M-112.1 -270.7 A293 293 0 0 1 112.1 -270.7"/>
    <path class="hub-segment" style="stroke:var(--seg-2)" d="M112.1 -270.7 A293 293 0 0 1 270.7 -112.1"/>
    <path class="hub-segment" style="stroke:var(--seg-3)" d="M270.7 -112.1 A293 293 0 0 1 270.7 112.1"/>
    <path class="hub-segment" style="stroke:var(--seg-4)" d="M270.7 112.1 A293 293 0 0 1 112.1 270.7"/>
    <path class="hub-segment" style="stroke:var(--seg-5)" d="M112.1 270.7 A293 293 0 0 1 -112.1 270.7"/>
    <path class="hub-segment" style="stroke:var(--seg-6)" d="M-112.1 270.7 A293 293 0 0 1 -270.7 112.1"/>
    <path class="hub-segment" style="stroke:var(--seg-7)" d="M-270.7 112.1 A293 293 0 0 1 -270.7 -112.1"/>
    <path class="hub-segment" style="stroke:var(--seg-8)" d="M-270.7 -112.1 A293 293 0 0 1 -112.1 -270.7"/>
    <g class="hub-dividers">
      <line class="hub-divider" x1="-100.3" y1="-242.1" x2="-124" y2="-299.3"/>
      <line class="hub-divider" x1="100.3" y1="-242.1" x2="124" y2="-299.3"/>
      <line class="hub-divider" x1="242.1" y1="-100.3" x2="299.3" y2="-124"/>
      <line class="hub-divider" x1="242.1" y1="100.3" x2="299.3" y2="124"/>
      <line class="hub-divider" x1="100.3" y1="242.1" x2="124" y2="299.3"/>
      <line class="hub-divider" x1="-100.3" y1="242.1" x2="-124" y2="299.3"/>
      <line class="hub-divider" x1="-242.1" y1="100.3" x2="-299.3" y2="124"/>
      <line class="hub-divider" x1="-242.1" y1="-100.3" x2="-299.3" y2="-124"/>
    </g>
  </g>

  <text class="hub-title">
    <tspan x="966" y="963">CHIEF FINANCIAL</tspan>
    <tspan x="966" y="1029">OFFICER</tspan>
  </text>

  <text class="node-label">
    <tspan x="966" y="312">Cost Accounting</tspan>
    <tspan x="966" y="355">&amp; Cost</tspan>
    <tspan x="966" y="398">Management</tspan>
  </text>
  <text class="node-label">
    <tspan x="1409" y="458">Capital</tspan>
    <tspan x="1409" y="502">Structure</tspan>
    <tspan x="1409" y="546">and the</tspan>
    <tspan x="1409" y="590">Cost of Capital</tspan>
  </text>
  <text class="node-label">
    <tspan x="1592" y="914">Long-term &amp;</tspan>
    <tspan x="1592" y="958">short-term</tspan>
    <tspan x="1592" y="1002">investment</tspan>
    <tspan x="1592" y="1045">decisions</tspan>
  </text>
  <text class="node-label">
    <tspan x="1414" y="1403">Performance</tspan>
    <tspan x="1414" y="1447">Evaluation</tspan>
  </text>
  <text class="node-label">
    <tspan x="971" y="1564">Budeting &amp;</tspan>
    <tspan x="971" y="1608">Strategic</tspan>
    <tspan x="971" y="1651">Planning</tspan>
  </text>
  <text class="node-label">
    <tspan x="523" y="1390">Risk</tspan>
    <tspan x="523" y="1434">Management</tspan>
  </text>
  <text class="node-label">
    <tspan x="340" y="935">Compliance :</tspan>
    <tspan class="regular" x="340" y="978">tax, legal</tspan>
    <tspan class="regular" x="340" y="1022">and regulatory</tspan>
  </text>
  <text class="node-label">
    <tspan x="523" y="453">Communication :</tspan>
    <tspan class="regular" x="523" y="497">Board of Directors,</tspan>
    <tspan class="regular" x="523" y="540">creditors, owners,</tspan>
    <tspan class="regular" x="523" y="584">investors, credit</tspan>
    <tspan class="regular" x="523" y="627">rating agencies</tspan>
  </text>
</svg>
</body>
</html>
```